Modern HomePage Design for Church

We are looking for a modern homepage design using the sections we put together in the template. The colors we want are blue, black, grey, and white. We do not want use the colors in the logo. Please modify the logo color to match the website color scheme.

Target Market(s)

Church

Industry/Entity Type

Church

Number of Pages Required

1 page

Colors
0293ce
ffffff
474747
9d9d9d

```html
<!DOCTYPE html>
<html lang="en">
<head>
<meta charset="utf-8">
<title>Wellspring Community Church</title>
<link href="https://fonts.googleapis.com/css2?family=Montserrat:wght@300;400;500;600;700;800&family=Yellowtail&display=swap" rel="stylesheet">
<style>
:root{
  --blue:#0293ce;
  --white:#ffffff;
  --dark:#474747;
  --grey:#9d9d9d;
  --black:#141414;
  --ink:#222222;
  --panel:#1c1c1c;
  --light:#f3f3f3;
}
*{box-sizing:border-box;margin:0;padding:0}
html,body{width:1200px;height:5056px;overflow:hidden}
body{font-family:'Montserrat',sans-serif;color:var(--dark);background:var(--white);position:relative}
section,header,footer{position:relative;width:1200px;overflow:hidden}
.abs{position:absolute}
.ph{position:absolute;display:block}
.btn{display:inline-block;background:var(--blue);color:var(--white);font-weight:600;font-size:15px;letter-spacing:1px;text-transform:uppercase;padding:12px 24px}
.brand{display:flex;align-items:center;gap:12px;color:var(--white);font-weight:600;font-size:40px;letter-spacing:2px}
.brand .dot{width:26px;height:26px;border-radius:50%;background:var(--blue)}
.brand small{display:block;font-size:13px;letter-spacing:2px;font-weight:600}

/* hero */
.hero{height:715px;background:var(--black)}
.hero .ph{inset:0;background:radial-gradient(ellipse at 70% 15%,#7a7a7a 0%,#3a3a3a 35%,#111 80%)}
.hero .brand{position:absolute;left:40px;top:40px}
.nav{position:absolute;right:40px;top:40px;display:flex;align-items:center;gap:28px;font-size:15px;font-weight:500;color:var(--white);text-transform:uppercase}
.nav .on{color:var(--blue)}
.nav .btn{font-size:14px;padding:10px 18px}
.times{position:absolute;right:40px;top:112px;display:flex;gap:22px}
.times span{background:#8a8a8a;color:var(--white);font-size:13px;font-weight:600;padding:9px 20px;text-transform:uppercase}
.hero-copy{position:absolute;left:0;right:0;top:330px;text-align:center;color:var(--white)}
.hero-copy .script{font-family:'Yellowtail',cursive;font-size:48px}
.hero-copy h1{font-size:76px;font-weight:800;letter-spacing:3px;line-height:1;margin-top:4px}
.hero-copy h2{font-size:30px;font-weight:700;letter-spacing:2px;margin-top:18px;padding-top:14px;border-top:2px solid var(--white);display:inline-block}
.hero-copy p{font-size:20px;font-weight:700;margin-top:18px}
.hero-copy .btn{margin-top:26px}

.visitors{height:87px;background:var(--dark);display:flex;align-items:center;justify-content:space-between;padding:0 50px;color:var(--white);font-size:17px;font-weight:500}
.visitors span.btn{background:var(--white);color:var(--ink);font-size:14px}

/* welcome */
.welcome{height:478px;background:var(--white)}
.welcome .copy{position:absolute;left:77px;top:60px;width:600px}
.welcome h2{font-size:46px;font-weight:400;color:var(--grey);letter-spacing:1px}
.welcome h3{font-size:22px;font-weight:700;color:var(--dark);margin-top:6px}
.welcome p{font-size:17px;line-height:1.55;margin-top:26px}
.welcome .sign{font-family:'Yellowtail',cursive;font-size:40px;color:var(--ink);margin-top:34px;border-bottom:2px solid var(--ink);display:inline-block}
.welcome .ph{right:0;top:0;width:492px;height:478px;background:linear-gradient(135deg,#d8d8d8,#8d8d8d 60%,#555)}

/* meeting */
.meeting{height:253px;background:#2a2a2a}
.meeting .cal{position:absolute;left:77px;top:62px}
.meeting .title{position:absolute;left:170px;top:58px;color:var(--white);font-size:27px;font-weight:300}
.meeting .title b{display:block;font-size:20px;font-weight:400}
.meeting .desc{position:absolute;left:77px;top:160px;width:520px;color:#cfcfcf;font-size:15px;line-height:1.45}
.count{position:absolute;left:640px;top:50px;display:flex}
.count div{width:120px;text-align:center;color:var(--white);border-left:1px solid #555}
.count div:first-child{border-left:0}
.count small{display:block;font-size:15px;letter-spacing:1px;color:#cfcfcf}
.count strong{display:block;font-size:42px;font-weight:400;margin-top:6px}
.meeting .btn{position:absolute;left:815px;top:182px;font-size:14px;padding:10px 22px}

/* beliefs */
.beliefs{height:374px;display:flex;justify-content:space-between;padding:95px 90px 0}
.belief{width:300px;text-align:center}
.belief h4{font-size:15px;font-weight:700;color:var(--ink);margin-top:18px}
.belief p{font-size:15px;line-height:1.4;margin-top:6px;color:var(--dark)}

/* involved */
.involved{height:483px;background:var(--panel)}
.tile{position:absolute;display:flex;align-items:flex-end;justify-content:center;padding-bottom:14px}
.tile b{background:rgba(0,0,0,.55);color:var(--white);font-size:13px;font-weight:700;padding:4px 8px;text-transform:uppercase}
.involved .copy{position:absolute;left:790px;top:150px;width:340px}
.involved h2{font-size:46px;font-weight:400;color:var(--white);letter-spacing:1px}
.involved h2 span{color:var(--blue)}
.involved p{font-size:16px;line-height:1.5;color:#888;margin-top:16px}

/* blog */
.blog{height:522px}
.blog .copy{position:absolute;left:77px;top:82px;width:460px}
.blog h2{font-size:46px;font-weight:500;color:var(--ink)}
.blog .date{font-size:15px;margin-top:34px;color:var(--ink)}
.blog h3{font-size:19px;font-weight:700;color:var(--blue);margin-top:26px}
.blog p{font-size:17px;line-height:1.5;margin-top:8px}
.blog .btn{margin-top:26px;font-size:14px}
.blog .ph{right:0;top:0;width:660px;height:522px;background:linear-gradient(90deg,#0e0e0e 0%,#2b1a0c 45%,#b3611a 75%,#f0b050 100%)}

/* pastor */
.pastor{height:540px;background:#1b1b1b}
.pastor .bgph{position:absolute;inset:0;background:linear-gradient(100deg,#1a1a1a 20%,#3b3b3b 50%,#1a1a1a 80%)}
.label{position:absolute;color:var(--blue);font-size:28px;font-weight:500;text-transform:uppercase}
.pastor .face{left:77px;top:145px;width:321px;height:321px;background:linear-gradient(160deg,#8d8d8d,#4a4a4a)}
.quote{position:absolute;left:421px;top:150px;width:280px;color:var(--white)}
.quote q{font-size:30px;line-height:1.3;font-weight:400}
.quote p{font-size:15px;line-height:1.45;color:#bdbdbd;margin-top:14px}
.quote cite{display:block;font-style:normal;font-size:14px;color:var(--grey);margin-top:18px}
.pod{position:absolute;left:805px;width:320px;display:flex;gap:14px;padding-bottom:14px;border-bottom:1px solid #555;color:#ddd;font-size:16px;line-height:1.35}
.pod i{flex:none;width:28px;height:28px;border:2px solid #ccc;display:flex;align-items:center;justify-content:center}
.pod small{display:block;color:var(--grey);font-size:14px}

/* events */
.events{height:717px;background:var(--white)}
.events h2{text-align:center;font-size:38px;font-weight:400;color:var(--ink);letter-spacing:1px;padding-top:85px}
.card{position:absolute;top:178px;width:323px;height:452px;background:var(--white);box-shadow:0 4px 14px rgba(0,0,0,.12)}
.card .ph{left:0;top:0;width:323px;height:232px}
.card .fold{position:absolute;right:0;top:0;width:0;height:0;border-left:62px solid transparent;border-top:62px solid var(--white)}
.card .pin{position:absolute;right:12px;top:10px;width:26px;height:26px;border-radius:50%;background:var(--blue)}
.card .date{position:absolute;left:0;top:232px;width:323px;height:50px;background:var(--blue);color:var(--white);display:flex;align-items:center;justify-content:center;gap:12px;font-size:20px;font-weight:600}
.card h3{position:absolute;left:24px;right:20px;top:302px;font-size:18px;font-weight:700;color:var(--ink);line-height:1.3}
.card ul{position:absolute;left:24px;top:365px;list-style:none;font-size:14px;color:var(--dark)}
.card li{display:flex;gap:10px;align-items:center;margin-bottom:7px}
.card .rule{position:absolute;left:0;right:0;bottom:0;height:4px;background:linear-gradient(90deg,var(--dark),var(--blue))}

/* widgets */
.widgets{height:572px;background:var(--panel);color:var(--white)}
.widgets h4{position:absolute;top:150px;font-size:21px;font-weight:500}
.item{position:absolute;display:flex;gap:14px;width:290px}
.item .thumb{flex:none;width:68px;height:68px;background:linear-gradient(135deg,#6b6b6b,#2f2f2f)}
.item b{display:block;color:var(--blue);font-weight:400;font-size:15px}
.item span{font-size:14px;color:#bbb;line-height:1.35}
.tags{position:absolute;left:438px;top:208px;width:330px;display:flex;flex-wrap:wrap;gap:8px}
.tags span{background:var(--blue);font-size:14px;padding:6px 12px}
.feed{position:absolute;left:438px;top:345px;width:330px;height:185px;background:linear-gradient(135deg,#5a5a5a,#262626);display:flex;align-items:center;justify-content:center;font-size:20px}

/* footer */
.foot{height:257px;background:var(--white)}
.foot .brand{position:absolute;left:91px;top:60px;color:var(--ink);font-size:38px}
.foot .brand small{color:var(--grey)}
.social{position:absolute;left:120px;top:166px;display:flex;gap:12px}
.social i{width:24px;height:24px;border-radius:50%;border:2px solid var(--grey)}
.foot .nav{top:102px;right:80px;color:var(--ink);font-size:14px;gap:24px}
.copyright{height:58px;background:var(--black);color:#ccc;font-size:12px;font-weight:600;text-align:center;line-height:58px;letter-spacing:1px}
</style>
</head>
<body>

<header class="hero">
  <div class="ph" role="img" aria-label="Crowd with raised hands at a worship service, black and white"></div>
  <div class="brand"><span class="dot"></span><div>WELLSPRING<small>COMMUNITY CHURCH</small></div></div>
  <nav class="nav">
    <span class="on">Home</span><span>Team</span><span>Features</span><span>Events</span><span>Sermons</span><span>Contact</span><span>Blog</span><span class="btn">Give Online</span>
  </nav>
  <div class="times"><span>Sunday Worship 10:15</span><span>Sunday School 09:00</span></div>
  <div class="hero-copy">
    <div class="script">A very special celebration is near</div>
    <h1>EASTER WEEK</h1>
    <h2>JOIN THE REMEMBERANCE</h2>
    <p>Service starting at 19:00 daily</p>
    <span class="btn">Continue Reading</span>
  </div>
</header>

<section class="visitors">
  <span>First time visitor? Find out how, where and when we worship. We hope to see you soon.</span>
  <span class="btn">Visitors Info</span>
</section>

<section class="welcome">
  <div class="copy">
    <h2>WELCOME TO</h2>
    <h3>WELLSPRING COMMUNITY CHURCH</h3>
    <p>Lorem ipsum dolor sit amet, consectetur adipiscing elit, sed do eius mod tempor incididunt ut labore et dolore magna ali qua. Ut enim ad minim veniam, quis nostrud exercitation ulla co laboris nisi ut aliquip ex ea commodo consequat.</p>
    <div class="sign">Pastor Daniel</div>
  </div>
  <div class="ph" role="img" aria-label="Smiling older couple embracing outdoors"></div>
</section>

<section class="meeting">
  <svg class="cal" width="66" height="66" viewBox="0 0 66 66" fill="none" stroke="var(--blue)" stroke-width="5"><rect x="4" y="10" width="58" height="52"/><path d="M18 3v14M48 3v14M20 36l9 9 17-17"/></svg>
  <div class="title">Church leaders meeting<b>March 27, 2019 - 07:00 pm</b></div>
  <p class="desc">Meeting for the church leaders. This is where we plan the strategy for the church and give feedback on projects.</p>
  <div class="count">
    <div><small>DAYS</small><strong>06</strong></div>
    <div><small>HOURS</small><strong>15</strong></div>
    <div><small>MINUTES</small><strong>26</strong></div>
    <div><small>SECONDS</small><strong>16</strong></div>
  </div>
  <span class="btn">Read More</span>
</section>

<section class="beliefs">
  <div class="belief">
    <svg width="70" height="76" viewBox="0 0 70 76" fill="none" stroke="var(--blue)" stroke-width="4"><path d="M35 2v16M28 9h14M35 18L12 38v36h46V38z"/><path d="M28 74V56h14v18M4 74h62"/></svg>
    <h4>WHAT WE BELIEVE</h4>
    <p>We believe in the existence of GOD and His Holy Word to be the foundation of our faith. It shall not be moved nor be compromised.</p>
  </div>
  <div class="belief">
    <svg width="70" height="76" viewBox="0 0 70 76" fill="none" stroke="var(--blue)" stroke-width="4"><path d="M35 72s24-22 24-42a24 24 0 0 0-48 0c0 20 24 42 24 42z"/><circle cx="35" cy="30" r="9"/></svg>
    <h4>SERVICES &amp; LOCATIONS</h4>
    <p>Riverton, GA 30100, USA<br>Sunday morning (08:15 - 12:00 PM)<br>Sunday afternoon (04:00 - 06:00 PM)<br>Wednesday (08:00 - 09:00 PM)</p>
  </div>
  <div class="belief">
    <svg width="70" height="76" viewBox="0 0 70 76" fill="none" stroke="var(--blue)" stroke-width="4"><path d="M35 40S18 28 18 18a9 9 0 0 1 17-4 9 9 0 0 1 17 4c0 10-17 22-17 22z"/><path d="M4 54h18l14 6h14a5 5 0 0 1 0 10H28M50 60l14-8"/></svg>
    <h4>GIVING</h4>
    <p>Lorem ipsum dolor sit amet, con sectetur adipiscing elit, sed do eiusmod tempor incididunt ut labore et dolore magna aliqua.</p>
  </div>
</section>

<section class="involved">
  <div class="tile" role="img" aria-label="Children smiling together" style="left:0;top:0;width:303px;height:240px;background:linear-gradient(135deg,#7d6a52,#3f4a56)"><b>Kids Ministry</b></div>
  <div class="tile" role="img" aria-label="Volunteers helping in the community" style="left:303px;top:0;width:219px;height:240px;background:linear-gradient(135deg,#9a9a9a,#474747)"><b>Outreach</b></div>
  <div class="tile" role="img" aria-label="Teenagers laughing together" style="left:522px;top:0;width:213px;height:240px;background:linear-gradient(135deg,#d9b48a,#8c6a4f)"><b>Teens Ministry</b></div>
  <div class="tile" role="img" aria-label="Open bible on a table" style="left:0;top:240px;width:303px;height:243px;background:linear-gradient(135deg,#6b5a46,#2a241e)"><b>Bible Study</b></div>
  <div class="tile" role="img" aria-label="Senior members of the congregation" style="left:303px;top:240px;width:432px;height:243px;background:linear-gradient(135deg,#8a8a8a,#3a3a3a)"><b>Seniors Ministry</b></div>
  <div class="copy">
    <h2><span>GET</span> INVOLVED</h2>
    <p>The success of our church depends on participation from people like you. Get involved in our ministries, it will change your life.</p>
  </div>
</section>

<section class="blog">
  <div class="copy">
    <h2>LATEST BLOG</h2>
    <div class="date">Jan 21, 2019</div>
    <h3>PRAY WITHOUT CEASING</h3>
    <p>Lorem ipsum dolor sit amet, consectetur adi piscing elit, sed do eiusmod tempor incididunt ut labore et dolore magna aliqua. Ut enim ad minim veniam, quis nostrud exercitation ulla co laboris nisi ut aliquip ex ea commodo.</p>
    <span class="btn">Read More</span>
  </div>
  <div class="ph" role="img" aria-label="Silhouette of a person praying against a sunset"></div>
</section>

<section class="pastor">
  <div class="bgph" role="img" aria-label="Open bible, dimmed background"></div>
  <div class="label" style="left:77px;top:78px">Pastor</div>
  <div class="ph face" role="img" aria-label="Portrait of the pastor"></div>
  <div class="quote">
    <q>One thing I asked of the Lord</q>
    <p>Lorem ipsum dolor sit amet, con sectetur adipiscing elit, sed doe iusmod tempor incididunt ut lab ore et dolore magna aliqua. Ut enim ad minim veniam, quis nos trud exercitation ullamco.</p>
    <cite>– Samuel Reed –</cite>
  </div>
  <div class="label" style="left:805px;top:78px">Podcast</div>
  <div class="pod" style="top:150px"><i><svg width="12" height="14"><path d="M0 0l12 7-12 7z" fill="#ccc"/></svg></i><div>Holy Spirit : Strategy Thinking<small>by Samuel Reed</small></div></div>
  <div class="pod" style="top:238px"><i><svg width="12" height="14"><path d="M0 0l12 7-12 7z" fill="#ccc"/></svg></i><div>Holy Spirit : Strategy Thinking<small>by Samuel Reed</small></div></div>
  <div class="pod" style="top:326px"><i><svg width="12" height="14"><path d="M0 0l12 7-12 7z" fill="#ccc"/></svg></i><div>Holy Spirit : Strategy Thinking<small>by Samuel Reed</small></div></div>
</section>

<section class="events">
  <h2>UPCOMING EVENTS</h2>
  <article class="card" style="left:91px">
    <div class="ph" role="img" aria-label="Wooden cross under a cloudy sky" style="background:linear-gradient(160deg,#d0d0d0,#5a5a5a)"></div>
    <span class="fold"></span><span class="pin"></span>
    <div class="date"><svg width="20" height="20" fill="none" stroke="#fff" stroke-width="2"><rect x="1" y="3" width="18" height="16"/><path d="M1 8h18M6 0v5M14 0v5"/></svg>Feb 22, 2019</div>
    <h3>Sharing our faith and love to children</h3>
    <ul><li>◷ Thursday 08:00 : 09:00 am</li><li>⌂ Wellspring Church</li><li>⊙ The Park, Riverton GA</li></ul>
    <span class="rule"></span>
  </article>
  <article class="card" style="left:438px">
    <div class="ph" role="img" aria-label="Open bible with a ribbon bookmark" style="background:linear-gradient(160deg,#3a2a26,#8a3030 60%,#1f1f1f)"></div>
    <span class="fold"></span><span class="pin"></span>
    <div class="date"><svg width="20" height="20" fill="none" stroke="#fff" stroke-width="2"><rect x="1" y="3" width="18" height="16"/><path d="M1 8h18M6 0v5M14 0v5"/></svg>Feb 18, 2019</div>
    <h3>Know Jesus Christ better through lines</h3>
    <ul><li>◷ Thursday 08:00 : 09:00 am</li><li>⌂ Wellspring Church</li><li>⊙ The Park, Riverton GA</li></ul>
    <span class="rule"></span>
  </article>
  <article class="card" style="left:785px">
    <div class="ph" role="img" aria-label="Group jumping at sunset" style="background:linear-gradient(180deg,#c9a06a,#e2b36c 55%,#3a2e22)"></div>
    <span class="fold"></span><span class="pin"></span>
    <div class="date"><svg width="20" height="20" fill="none" stroke="#fff" stroke-width="2"><rect x="1" y="3" width="18" height="16"/><path d="M1 8h18M6 0v5M14 0v5"/></svg>Feb 12, 2019</div>
    <h3>Caring about serving and the community</h3>
    <ul><li>◷ Thursday 08:00 : 09:00 am</li><li>⌂ Wellspring Church</li><li>⊙ The Park, Riverton GA</li></ul>
    <span class="rule"></span>
  </article>
</section>

<section class="widgets">
  <h4 style="left:77px">Latest Sermons</h4>
  <div class="item" style="left:77px;top:215px"><span class="thumb" role="img" aria-label="Sermon thumbnail"></span><div><b>All things are possible</b><span>Lorem ipsum dolor sit amet, consectetur.</span></div></div>
  <div class="item" style="left:77px;top:305px"><span class="thumb" role="img" aria-label="Sermon thumbnail"></span><div><b>Abounding the work of Lord</b><span>Lorem ipsum dolor sit amet, consectetur.</span></div></div>
  <h4 style="left:438px">Sermons Tags</h4>
  <div class="tags"><span>Faith</span><span>Forgiveness</span><span>Goodheartedness</span><span>Kindness</span><span>Love</span><span>Peace</span><span>Understanding</span></div>
  <div class="feed" role="img" aria-label="Audio feed banner">Podcast Feed</div>
  <h4 style="left:820px">Latest News</h4>
  <div class="item" style="left:820px;top:215px"><span class="thumb" role="img" aria-label="News thumbnail"></span><div><b>Holy Spirit</b><span>Lorem ipsum dolor sit amet, consectetur.</span></div></div>
  <div class="item" style="left:820px;top:305px"><span class="thumb" role="img" aria-label="News thumbnail"></span><div><b>Holy Spirit</b><span>Lorem ipsum dolor sit amet, consectetur.</span></div></div>
</section>

<footer class="foot">
  <div class="brand"><span class="dot"></span><div>WELLSPRING<small>COMMUNITY CHURCH</small></div></div>
  <div class="social"><i></i><i></i><i></i></div>
  <nav class="nav"><span>Home</span><span>Team</span><span>Features</span><span>Events</span><span>Sermons</span><span>Contact</span><span>Blog</span><span class="btn">Give Online</span></nav>
</footer>
<div class="copyright">COPYRIGHT © 2019 WELLSPRING COMMUNITY CHURCH. ALL RIGHTS RESERVED.</div>

</body>
</html>
```